Church Lanterns Over Millbrook Gospel Booklet Design

We need a booklet designed that we will be printing to hand out in our community. Wording for each page will be provided and we need graphic design to produce the layouts in a format ready for print. Booklet will be 4.75" x 4.75" square and a total of 12 pages: 1 cover page front, 1 cover page back, 10 inside pages some of which will be full spread across 2 pages.

Target Market(s)

English speaking Westerners

Industry/Entity Type

Religious

Font styles to use
Serif

Colors
ffffff
85abd2
0292cd
33b8a4
5c5c5c

Requirements
Must have
• Minimalist design with clean look described in attached document
Nice to have
• Aesthetically pleasing graphics, crisp fonts, excellent turn around times
Should not have
• Effeminate design, busy look with too much graphic and text

```html
<!DOCTYPE html>
<html lang="en">
<head>
<meta charset="utf-8">
<title>Lanterns Over Millbrook — Gospel Booklet Spread</title>
<link href="https://fonts.googleapis.com/css2?family=Libre+Caslon+Text:ital,wght@0,400;1,400&display=swap" rel="stylesheet">
<style>
  :root {
    --paper: #ffffff;
    --sky: #85abd2;
    --ink: #1a1a1a;
    --accent: #85abd2;
  }
  html, body {
    margin: 0;
    padding: 0;
    width: 1200px;
    height: 600px;
    overflow: hidden;
    background: var(--paper);
  }
  .spread {
    position: relative;
    width: 1200px;
    height: 600px;
    overflow: hidden;
    font-family: "Libre Caslon Text", Georgia, serif;
    color: var(--ink);
  }
  .spread__backdrop {
    position: absolute;
    inset: 0;
  }
  .page-text {
    position: absolute;
    margin: 0;
    text-align: center;
    font-style: italic;
    font-size: 21.5px;
    line-height: 30px;
  }
  .page-text--left {
    left: 70px;
    top: 170px;
    width: 460px;
  }
  .page-text--right {
    left: 690px;
    top: 30px;
    width: 420px;
  }
  .scripture {
    position: absolute;
    left: 680px;
    top: 318px;
    width: 440px;
    margin: 0;
    text-align: center;
    color: var(--accent);
    font-variant: small-caps;
    font-size: 23px;
    line-height: 34px;
    letter-spacing: 0.04em;
  }
  .scripture__ref {
    position: absolute;
    left: 800px;
    top: 538px;
    width: 200px;
    margin: 0;
    text-align: center;
    font-variant: small-caps;
    font-size: 16px;
    color: var(--ink);
  }
</style>
</head>
<body>
<main class="spread">
  <svg class="spread__backdrop" width="1200" height="600" viewBox="0 0 1200 600" aria-hidden="true">
    <defs>
      <linearGradient id="sky-fade" x1="0" y1="0" x2="0" y2="1">
        <stop offset="0" stop-color="#85abd2"/>
        <stop offset="0.3" stop-color="#ffffff"/>
        <stop offset="0.7" stop-color="#ffffff"/>
        <stop offset="1" stop-color="#85abd2"/>
      </linearGradient>
    </defs>
    <rect width="1200" height="600" fill="url(#sky-fade)"/>
    <circle cx="300" cy="300" r="350" fill="#ffffff"/>
    <circle cx="900" cy="300" r="350" fill="#ffffff"/>
  </svg>

  <p class="page-text page-text--left">This alienation from God is evident in a myriad of ways including poverty, crime, conflict in our relationships, and our internal struggles. But worse, when we die, we must face the consequences for our rejection of God by spending eternity in hell – a lake of fire created by God as the place where our treason is brought to justice.</p>

  <p class="page-text page-text--right">But God does not want you to pay for your own sins. God loves us so much he sent his only son to save us. Jesus Christ died on the cross to serve our sentence for our rebellion against God and rose again on the third day. Since Christ paid our full penalty, we can be completely forgiven and reconciled to God.</p>

  <blockquote class="scripture">“For God so loved the world that he sent his one and only son that whosoever believes in him will not perish but have eternal life.”</blockquote>
  <p class="scripture__ref">(John 3:16)</p>
</main>
</body>
</html>
```